Buch-/E-Book-Cover für Ausbildung und Weiterbildung von angehenden Sommeliers und Connaisseurs in der Spirituosenbranche
Zielgruppe
Ausbildung und Weiterbildung von angehenden Sommeliers und Connaisseurs in der Spirituosenbranche. Zielgruppe sind die Teilnehmer der genannten Kurse, Interessierte, Brenner und Gastronomen.
Aufgabenstellung
Klassisches, edles Design, klares Design, keine Bilder, Typografie steht im Vordergrund. Typografie in Relief.
A4
Vom Stil wie die angehängte Datei
Buchtitel: Kernwasser (groß) - verschnörkelt -
Hintergrund - Blautöne
Schrift: Titel Silber Untertitel: grau
Unterüberschrift: Kultur und Genuss
Autoren: Lehmkuhl • Wittrock
Buchrücken: Oben: Lehmkuhl Wittrock - Quer: Kernwasser - Unten: Amber Vessels

```html
<!DOCTYPE html>
<html lang="de">
<head>
<meta charset="utf-8">
<title>Kernwasser – Kultur und Genuss</title>
<link rel="stylesheet" href="https://fonts.googleapis.com/css2?family=Noto+Serif:ital,wght@0,700;1,700&family=Fira+Sans+Condensed:wght@500&family=Source+Sans+3:wght@400&display=swap">
<style>
  :root {
    --stage: #d6d5d3;
    --cover-top: #1d3557;
    --cover-bottom: #14253f;
    --silver: #c9ced6;
    --silver-light: rgba(255, 255, 255, 0.35);
    --silver-dark: rgba(0, 0, 0, 0.45);
    --grey: #a3abb8;
    --rule: #8f99a8;
    --author: #b4bbc6;
  }
  * { margin: 0; padding: 0; box-sizing: border-box; }
  html, body {
    width: 1200px;
    height: 1200px;
    overflow: hidden;
    background: var(--stage);
  }
  .cover {
    position: absolute;
    left: 299px;
    top: 48px;
    width: 602px;
    height: 1104px;
    background: linear-gradient(180deg, var(--cover-top), var(--cover-bottom));
    box-shadow: 0 6px 18px rgba(0, 0, 0, 0.2);
    text-align: center;
  }
  .cover__title {
    position: absolute;
    top: 92px;
    left: 0;
    right: 0;
    font-family: "Noto Serif", Georgia, serif;
    font-weight: 700;
    font-size: 70px;
    line-height: 84px;
    letter-spacing: -1px;
    color: var(--silver);
    text-shadow: -1px -1px 0 var(--silver-light), 2px 2px 2px var(--silver-dark);
  }
  .cover__subtitle {
    position: absolute;
    top: 188px;
    left: 0;
    right: 0;
    font-family: "Fira Sans Condensed", "Arial Narrow", sans-serif;
    font-weight: 500;
    font-size: 25px;
    line-height: 30px;
    letter-spacing: 3px;
    color: var(--grey);
  }
  .cover__rule {
    position: absolute;
    top: 242px;
    left: 48px;
    width: 506px;
    height: 3px;
    background: var(--rule);
    box-shadow: 0 1px 0 var(--silver-dark);
  }
  .cover__audience {
    position: absolute;
    top: 300px;
    left: 0;
    right: 0;
    font-family: "Noto Serif", Georgia, serif;
    font-style: italic;
    font-weight: 700;
    font-size: 26px;
    line-height: 32px;
    color: var(--silver);
    text-shadow: -1px -1px 0 var(--silver-light), 1px 1px 2px var(--silver-dark);
  }
  .cover__authors {
    position: absolute;
    top: 1008px;
    left: 0;
    right: 0;
    font-family: "Source Sans 3", Arial, sans-serif;
    font-size: 16px;
    letter-spacing: 0.5px;
    color: var(--author);
  }
</style>
</head>
<body>
  <main class="cover">
    <h1 class="cover__title">KERNWASSER</h1>
    <p class="cover__subtitle">KULTUR UND GENUSS</p>
    <div class="cover__rule"></div>
    <p class="cover__audience">für<br>Sommeliers<br>&amp;<br>Connaisseurs</p>
    <p class="cover__authors">Lehmkuhl • Wittrock</p>
  </main>
</body>
</html>
```